Mirela Dawn Business Card Design

I need a business card for my daughter. She has it all described in the file below. But it needs to be square in shape. http://www.mireladawn.example is her web site

Target Market(s)

18-35 year old women

Industry/Entity Type

Fashion

Contact Information for Business Card

Please look at the attached file as it has all the details.

Requirements
Must have
• Please look at the attached file as it has all the details.
Nice to have
Should not have

```html
<!DOCTYPE html>
<html lang="en">
<head>
<meta charset="utf-8">
<title>Mirela Dawn – Business Card</title>
<link rel="stylesheet" href="https://fonts.googleapis.com/css2?family=Playfair+Display:wght@900&family=Lato:wght@400&family=Tinos:wght@400&display=swap">
<style>
  :root {
    --stage: #1d1d1d;
    --card-dark: #2a2a2a;
    --marble-black: #0d0b08;
    --marble-gold: #8a7238;
    --blush: #f8cbd8;
    --name-pink: #f6c4d1;
    --ink: #1a1a1a;
    --white: #ffffff;
  }
  * { box-sizing: border-box; margin: 0; padding: 0; }
  html, body { width: 1200px; height: 741px; overflow: hidden; background: var(--stage); }
  .canvas { position: relative; width: 1200px; height: 741px; }

  /* Front of card */
  .card-front {
    position: absolute; left: 220px; top: 176px; width: 360px; height: 360px; overflow: hidden;
  }
  .marble-texture {
    position: absolute; inset: 0;
    background:
      radial-gradient(ellipse at 20% 85%, rgba(138,114,56,.55), transparent 45%),
      radial-gradient(ellipse at 80% 20%, rgba(138,114,56,.45), transparent 50%),
      radial-gradient(ellipse at 55% 55%, rgba(138,114,56,.25), transparent 55%),
      var(--marble-black);
  }
  .front-brand { position: absolute; left: 0; right: 0; top: 147px; text-align: center; }
  .front-name {
    font-family: "Playfair Display", "Times New Roman", serif; font-weight: 900;
    font-size: 38px; color: var(--name-pink); line-height: 1;
    text-transform: uppercase;
  }
  .front-tagline {
    font-family: "Lato", Arial, sans-serif; font-size: 15px; letter-spacing: 2px;
    color: var(--white); margin-top: 22px; text-transform: lowercase;
  }

  /* Back of card */
  .card-back {
    position: absolute; left: 624px; top: 176px; width: 358px; height: 358px;
    background: var(--card-dark);
  }
  .info-panel {
    position: absolute; left: 18px; top: 18px; width: 321px; height: 274px;
    background: var(--blush);
  }
  .back-name {
    position: absolute; left: 0; right: 0; top: 30px; text-align: center;
    font-family: "Playfair Display", "Times New Roman", serif; font-weight: 900;
    font-size: 30px; color: var(--ink); line-height: 1; text-transform: uppercase;
  }
  .back-tagline {
    position: absolute; left: 0; right: 0; top: 80px; text-align: center;
    font-family: "Lato", Arial, sans-serif; font-size: 13px; letter-spacing: 1.6px; color: var(--ink);
  }
  .contact-list {
    position: absolute; left: 31px; top: 125px; list-style: none;
    font-family: "Lato", Arial, sans-serif; font-size: 16px; color: var(--ink); line-height: 20.7px;
  }
  .contact-item { display: flex; align-items: center; white-space: nowrap; }
  .contact-dot {
    width: 15px; height: 15px; border-radius: 50%; background: var(--white);
    margin-right: 13px; flex: none;
  }
  .contact-label {
    font-family: "Tinos", "Times New Roman", serif; font-size: 13px; color: var(--white);
    text-transform: uppercase; margin-right: 3px;
  }
  .web-address {
    position: absolute; left: 0; right: 0; top: 298px; text-align: center;
    font-family: "Lato", Arial, sans-serif; font-size: 15.5px; letter-spacing: 1.6px; color: var(--white);
  }
  .accent-bar {
    position: absolute; left: 18px; width: 321px; top: 326px; height: 12px; background: var(--blush);
  }
</style>
</head>
<body>
<main class="canvas">

  <section class="card-front" aria-label="Card front">
    <div class="marble-texture" role="img" aria-label="Black marble texture with gold veining"></div>
    <div class="front-brand">
      <h1 class="front-name">Mirela Dawn</h1>
      <p class="front-tagline">dress with intention</p>
    </div>
  </section>

  <section class="card-back" aria-label="Card back">
    <div class="info-panel">
      <h2 class="back-name">Mirela Dawn</h2>
      <p class="back-tagline">dress with intention</p>
      <ul class="contact-list">
        <li class="contact-item"><span class="contact-dot"></span>picfeed.example/mireladawnxo</li>
        <li class="contact-item"><span class="contact-dot"></span>chirpline.example/mireladawnxo</li>
        <li class="contact-item"><span class="contact-dot"></span>@mireladawnxo</li>
        <li class="contact-item"><span class="contact-dot"></span>mirela@mireladawnxo</li>
        <li class="contact-item"><span class="contact-label">Blog:</span>mireladawn.example</li>
        <li class="contact-item"><span class="contact-label">Video:</span>vidstream.example/mireladawn</li>
      </ul>
    </div>
    <p class="web-address">www.mireladawn.example</p>
    <div class="accent-bar"></div>
  </section>

</main>
</body>
</html>
```